new website for ISP and tech consultant

Our company is a wireless Internet Service Provider as well as a technology consultant. We need a new website that is modern looking and something that I can make responsive and mobile friendly. All the pages that are at on our current website (qwelrit.com) must also exist on the new site so please allow space for navigation for them in the design.

It's OK to change logo color

Target Market(s)

Rural internet customers

Industry/Entity Type

Internet Service Provider

Number of Pages Required

1 page

Font styles to use
Sans Serif

Requirements
Must have
• Please keep in mind with the design will need to be able to be made mobile friendly and responsive.
• I'd like an "edge to edge" look in the browser.
• Integrate our logo and the "field" picture (attached)
Should not have
• stock photos (as little as possible)

```html
<!DOCTYPE html>
<html lang="en">
<head>
<meta charset="utf-8">
<title>Qwelrit — Wireless Internet &amp; Technology Consulting</title>
<link href="https://fonts.googleapis.com/css2?family=Roboto:wght@300;400;500&family=Roboto+Condensed:wght@400&family=Oswald:wght@300;400&display=swap" rel="stylesheet">
<style>
:root{
  --brand:#7891cc;
  --link:#2b5d9c;
  --ink:#222;
  --muted:#666;
  --paper:#fff;
  --tint:#eef1f7;
  --night:#111;
  --hero-top:#4f7cc4;
  --hero-mid:#5b6f45;
  --hero-low:#4a3c2c;
  --soil:#2e2a22;
}
*{box-sizing:border-box;margin:0;padding:0}
html,body{width:846px;height:1200px;overflow:hidden}
body{position:relative;font-family:'Roboto',sans-serif;color:var(--ink);background:var(--paper)}
.abs{position:absolute}

/* hero */
.hero{left:0;top:0;width:846px;height:421px;background:linear-gradient(180deg,var(--hero-top) 0%,var(--hero-mid) 60%,var(--hero-low) 100%)}
.topbar{left:130px;top:28px;width:656px;height:50px;background:var(--paper);box-shadow:0 2px 6px rgba(0,0,0,.2)}
.menu{left:162px;top:28px;height:50px;display:flex;align-items:center;list-style:none;font-size:10px}
.menu li{margin-right:23px;color:var(--ink)}
.menu li.active{color:var(--brand)}
.search{left:750px;top:28px;width:36px;height:50px;background:var(--brand);display:flex;align-items:center;justify-content:center}
.logo{left:56px;top:12px;width:72px;height:72px;border-radius:50%;background:var(--paper);border:6px solid var(--brand);display:flex;align-items:center;justify-content:center;font-weight:500;font-size:12px;color:var(--brand)}
.hero-title{left:95px;top:178px;font-family:'Oswald',sans-serif;color:#fff;text-shadow:0 1px 3px rgba(0,0,0,.4)}
.hero-title .big{font-size:32px;line-height:39px;font-weight:400;letter-spacing:-.5px}
.hero-title .sub{font-size:27px;font-weight:300;margin-top:4px;letter-spacing:-.3px}
.wifi{left:228px;top:148px}
.arrow{top:196px}
.showcase{left:440px;top:124px;width:327px;height:250px;border-radius:6px;background:linear-gradient(180deg,#6f8fc8 0%,#7c7a55 100%);display:flex;align-items:center;justify-content:center;padding-bottom:60px;font-family:'Oswald',sans-serif;font-size:25px;color:#fff;text-shadow:0 1px 3px rgba(0,0,0,.5)}

/* services */
.services{left:0;top:421px;width:846px;height:273px;background:var(--soil)}
.section-title{left:0;top:442px;width:846px;text-align:center;color:#fff;font-size:17px;font-weight:500}
.card{top:476px;width:176px;height:190px;background:var(--paper);text-align:center}
.card .icon{margin:10px auto 0;width:76px;height:76px;border-radius:50%;border:3px solid #fff;box-shadow:0 0 0 1px #ccc;background:var(--brand);display:flex;align-items:center;justify-content:center}
.card h3{font-family:'Roboto Condensed',sans-serif;font-weight:400;font-size:12px;margin-top:12px}
.card p{font-size:8px;line-height:13px;color:var(--muted);padding:0 20px;margin-top:12px}
.card .more{position:absolute;left:0;bottom:0;width:100%;height:29px;background:var(--brand);color:#fff;font-size:9px;line-height:29px}

/* news */
.news{left:0;top:694px;width:846px;height:300px;background:var(--tint)}
.heading{font-size:14px;font-weight:400}
.feed-img{left:62px;width:122px;height:91px;border:2px solid #fff;box-shadow:0 2px 4px rgba(0,0,0,.2)}
.feed-text{left:198px;width:220px}
.feed-text h4{font-size:11px;font-weight:400;color:var(--link);line-height:16px}
.feed-text .time{font-size:9px;margin:10px 0;display:flex;align-items:center;gap:4px}
.feed-text p{font-size:8px;line-height:15px;color:#444}
.divider{left:62px;top:846px;width:265px;border-top:1px dotted #bbb}
.promo{left:444px;top:754px;width:340px;height:202px;background:#f5f5f5;box-shadow:0 3px 8px rgba(0,0,0,.15)}
.promo-img{left:444px;top:754px;width:187px;height:202px;background:linear-gradient(180deg,#2d5584,#14264a)}
.promo-text{left:647px;top:766px;width:128px}
.promo-text h4{font-size:11.5px;font-weight:400;line-height:17px}
.promo-text p{font-size:7.2px;line-height:13px;color:#333;margin-top:8px;text-align:justify}
.info{display:flex;align-items:center;gap:6px;font-size:7.5px;margin-top:10px}

/* footer */
.footer{left:0;top:994px;width:846px;height:158px;background:var(--brand);color:#fff}
.fcol{top:1023px}
.fcol h5{font-size:11px;font-weight:400;margin-bottom:14px}
.fcol p{font-size:8px;line-height:13px}
.tweet{padding-left:19px}
.email-field{width:152px;height:22px;background:#f2f2f2;border:1px solid #ccc;font-size:7px;color:#555;padding:6px 8px;margin-top:6px}
.subscribe{margin-top:8px;width:67px;height:21px;background:linear-gradient(#fafafa,#ddd);border-radius:2px;color:#333;font-size:8px;font-weight:500;text-align:center;line-height:21px}
.social{display:flex;align-items:center;gap:10px;font-size:8.5px;margin-bottom:9px}
.social .dot{width:22px;height:22px;border-radius:50%;border:1.5px solid #fff}
.bottom{left:0;top:1152px;width:846px;height:48px;background:var(--night);color:#fff;font-size:8.5px;text-align:center;line-height:48px}
</style>
</head>
<body>

<!-- hero -->
<div class="abs hero" role="img" aria-label="Photo of a rural road between farm fields under a blue sky"></div>
<div class="abs topbar"></div>
<ul class="abs menu">
  <li class="active">HOME</li><li>INTERNET</li><li>SERVICES</li><li>PRODUCTS</li><li>PAY YOUR BILL</li><li>EMAIL</li><li>SUPPORT</li><li>CONTACT</li><li>NEWS</li>
</ul>
<div class="abs search"><svg width="12" height="12" viewBox="0 0 12 12"><circle cx="5" cy="5" r="3.6" fill="none" stroke="#fff" stroke-width="1.6"/><line x1="7.6" y1="7.6" x2="11" y2="11" stroke="#fff" stroke-width="1.8"/></svg></div>
<div class="abs logo">QWELRIT</div>

<svg class="abs arrow" style="left:24px" width="18" height="40" viewBox="0 0 18 40"><polyline points="17,1 1,20 17,39" fill="none" stroke="#fff" stroke-width="1.2"/></svg>
<svg class="abs arrow" style="left:804px" width="18" height="40" viewBox="0 0 18 40"><polyline points="1,1 17,20 1,39" fill="none" stroke="#fff" stroke-width="1.2"/></svg>

<svg class="abs wifi" width="86" height="64" viewBox="0 0 86 64">
  <g fill="none" stroke="#fff" stroke-width="8" stroke-linecap="round">
    <path d="M6 24 A52 52 0 0 1 80 24"/><path d="M20 37 A32 32 0 0 1 66 37"/><path d="M33 49 A14 14 0 0 1 53 49"/>
  </g><circle cx="43" cy="58" r="5" fill="#fff"/>
</svg>
<div class="abs hero-title">
  <div class="big">HIGH-SPEED</div>
  <div class="big">WIRELESS INTERNET</div>
  <div class="sub">Technology Consultant</div>
</div>

<div class="abs showcase" role="img" aria-label="Desktop monitor showing the farm field photo">EXPERTS IN THE FIELD</div>

<!-- services -->
<div class="abs services" role="img" aria-label="Darkened photo of ploughed field rows"></div>
<div class="abs section-title">OUR SERVICES</div>

<div class="abs card" style="left:62px">
  <div class="icon"><svg width="30" height="30" viewBox="0 0 30 30"><path d="M20 3a7 7 0 0 0-6.5 9.5L4 22l4 4 9.5-9.5A7 7 0 0 0 27 10l-4 4-4-1-1-4 4-4a7 7 0 0 0-2-2z" fill="#fff"/></svg></div>
  <h3>REPAIRS</h3>
  <p>Lorem Ipsum has been the industry's standard dummy text ever since the</p>
  <div class="more">Read More &gt;&gt;</div>
</div>
<div class="abs card" style="left:244px">
  <div class="icon"><svg width="32" height="24" viewBox="0 0 32 24"><g fill="none" stroke="#fff" stroke-width="3" stroke-linecap="round"><path d="M3 9a19 19 0 0 1 26 0"/><path d="M8 14a12 12 0 0 1 16 0"/><path d="M12.5 18.5a5 5 0 0 1 7 0"/></g><circle cx="16" cy="22" r="2" fill="#fff"/></svg></div>
  <h3>NETWORKING</h3>
  <p>Lorem Ipsum has been the industry's standard dummy text ever since the</p>
  <div class="more">Read More &gt;&gt;</div>
</div>
<div class="abs card" style="left:426px">
  <div class="icon"><svg width="34" height="28" viewBox="0 0 34 28" fill="#fff"><circle cx="17" cy="7" r="5"/><circle cx="7" cy="9" r="4"/><circle cx="27" cy="9" r="4"/><path d="M9 26c0-7 3.5-11 8-11s8 4 8 11z"/><path d="M0 24c0-6 3-9 7-9 2 0 3 .5 4 1.5-2 2-3 5-3 7.5z"/><path d="M34 24c0-6-3-9-7-9-2 0-3 .5-4 1.5 2 2 3 5 3 7.5z"/></svg></div>
  <h3>CONSULTING</h3>
  <p>Lorem Ipsum has been the industry's standard dummy text ever since the</p>
  <div class="more">Read More &gt;&gt;</div>
</div>
<div class="abs card" style="left:608px">
  <div class="icon"><svg width="32" height="28" viewBox="0 0 32 28"><rect x="2" y="2" width="28" height="18" rx="2" fill="none" stroke="#fff" stroke-width="3"/><rect x="13" y="20" width="6" height="4" fill="#fff"/><rect x="8" y="24" width="16" height="3" fill="#fff"/></svg></div>
  <h3>CUSTOM PROGRAMMING</h3>
  <p>Lorem Ipsum has been the industry's standard dummy text ever since the</p>
  <div class="more">Read More &gt;&gt;</div>
</div>

<!-- news -->
<div class="abs news"></div>
<svg class="abs" style="left:62px;top:724px" width="16" height="16" viewBox="0 0 16 16"><rect width="16" height="16" rx="3" fill="#f39a2b"/><circle cx="4.5" cy="11.5" r="1.6" fill="#fff"/><path d="M3 7a6 6 0 0 1 6 6M3 3.5a9.5 9.5 0 0 1 9.5 9.5" fill="none" stroke="#fff" stroke-width="1.8"/></svg>
<div class="abs heading" style="left:86px;top:724px">LIVE NEWS FEED</div>

<div class="abs feed-img" style="top:755px;background:linear-gradient(135deg,#dbe9fb,#8fb8ea)" role="img" aria-label="Illustration of a laptop with digital light lines"></div>
<div class="abs feed-text" style="top:752px">
  <h4>Streamtube problems</h4>
  <div class="time"><svg width="8" height="8" viewBox="0 0 8 8"><circle cx="4" cy="4" r="3.2" fill="none" stroke="#222" stroke-width="1"/><path d="M4 2v2h1.6" fill="none" stroke="#222" stroke-width=".9"/></svg>19.00 pm - 21.00 pm</div>
  <p>Streamtube has been having problems the last few days. Much of it looks to be on the east coast, how...</p>
</div>
<div class="abs divider"></div>

<div class="abs feed-img" style="top:866px;background:linear-gradient(135deg,#1456a8,#3a86d8)" role="img" aria-label="Illustration of connected computers on a blue network"></div>
<div class="abs feed-text" style="top:866px">
  <h4>Vendorsoft to axe Web Navigator<br>Scheduled Maintenance</h4>
  <div class="time"><svg width="8" height="8" viewBox="0 0 8 8"><circle cx="4" cy="4" r="3.2" fill="none" stroke="#222" stroke-width="1"/><path d="M4 2v2h1.6" fill="none" stroke="#222" stroke-width=".9"/></svg>19.00 pm - 21.00 pm</div>
  <p>We will be performing network maintenance on 3/12/15 from 12:00 AM to 06:00 AM. You may experienc...</p>
</div>

<div class="abs heading" style="left:444px;top:724px">QWELRIT HIGH-SPEED INTERNET</div>
<div class="abs promo"></div>
<div class="abs promo-img" role="img" aria-label="Illustration of a tablet with a networked globe"></div>
<div class="abs promo-text">
  <h4>High-Speed wireless Internet starting at $49.95/month</h4>
  <p>Lorem Ipsum has been the industry's standard dummy text ever since the 1500s, when an unknown printer took a galley of type and scrambled it to make a type specimen book.</p>
  <p style="text-align:left">NO arbitrary data cap! * No hidden fees!</p>
  <div class="info"><svg width="20" height="20" viewBox="0 0 20 20"><circle cx="10" cy="10" r="9.5" fill="#2f6fd0"/><circle cx="10.5" cy="5.5" r="1.5" fill="#fff"/><rect x="9" y="8.5" width="3" height="7" fill="#fff"/></svg>full information here</div>
</div>

<!-- footer -->
<div class="abs footer"></div>
<div class="abs fcol" style="left:61px">
  <h5>NEWSLETTERS SIGN UP</h5>
  <p>Sign up for our daily email by entering<br>your information below</p>
  <div class="email-field">Email address</div>
  <div class="subscribe">SUBSCRIBE</div>
</div>
<div class="abs fcol" style="left:271px">
  <h5>LATEST TWEET</h5>
  <p class="tweet">Featured Workspace : Bluefoundry<br><i style="line-height:24px">&nbsp;lnkr.to/8QpRzw"</i><br>10 hours ago</p>
</div>
<div class="abs fcol" style="left:480px">
  <h5>GET IN TOUCH</h5>
  <p>&nbsp;Address : 1200 Meadow Lane,<br>&nbsp;Fairview Plains, KS</p>
  <p style="margin-top:10px">&nbsp;Phone : 555 014 2277</p>
  <p style="margin-top:10px">&nbsp;Email : info@qwelrit.com</p>
</div>
<div class="abs fcol" style="left:677px">
  <h5>FOLLOW US ON</h5>
  <div class="social"><span class="dot"></span>Facelink</div>
  <div class="social"><span class="dot"></span>Chirper</div>
  <div class="social"><span class="dot"></span>Snapgram</div>
</div>
<div class="abs bottom">Copyright © 2015. All Rights Reserved</div>

</body>
</html>
```